Business Cards

Business card design for my company.
I would like the card's background colour to be black. You can also see our web site to get an idea of our brand. https://www.dlqmarrowfield.com.au/
- Name
- Email

```html
<!DOCTYPE html>
<html lang="en">
<head>
<meta charset="utf-8">
<title>DLQ Marrowfield – Business Cards</title>
<link rel="stylesheet" href="https://fonts.googleapis.com/css2?family=Poppins:wght@600;700&family=Questrial&display=swap">
<style>
  :root {
    --stage: #5b5d5e;
    --card-black: #0b0b0b;
    --panel-dark: #222222;
    --green: #0f9447;
    --green-light: #13ab4c;
    --white: #ffffff;
    --ink: #111111;
    --text-grey: #2a2a2a;
  }
  * { margin: 0; padding: 0; box-sizing: border-box; }
  html, body { width: 1200px; height: 780px; overflow: hidden; }
  body {
    background: var(--stage);
    display: flex;
    align-items: center;
    justify-content: center;
    gap: 40px;
    font-family: "Questrial", sans-serif;
  }
  .card {
    position: relative;
    width: 540px;
    height: 310px;
    border-radius: 18px;
    overflow: hidden;
  }

  /* Back side */
  .card-back { background: var(--card-black); }
  .back-pattern {
    position: absolute; inset: 0;
    background: radial-gradient(ellipse at 40% 55%, #2b3a31 0%, #141a16 55%, var(--card-black) 100%);
  }
  .back-brand {
    position: absolute;
    left: 0; right: 0; top: 50%;
    transform: translateY(-50%);
    display: flex; align-items: center; justify-content: center; gap: 14px;
  }
  .brand-square { width: 18px; height: 18px; background: var(--green); }
  .brand-name {
    font-family: "Poppins", sans-serif;
    font-weight: 600;
    color: var(--white);
    letter-spacing: 3px;
    white-space: nowrap;
  }
  .back-brand .brand-name { font-size: 30px; }

  /* Front side */
  .card-front { background: var(--white); }
  .front-shapes { position: absolute; inset: 0; }
  .front-brand {
    position: absolute;
    left: 26px; top: 208px;
    display: flex; align-items: center; gap: 10px;
  }
  .front-brand .brand-name { font-size: 15px; letter-spacing: 1.5px; }

  .person {
    position: absolute;
    right: 36px; top: 36px;
    text-align: right;
  }
  .person-name {
    font-family: "Poppins", sans-serif;
    font-weight: 700;
    font-size: 22px;
    color: var(--ink);
    line-height: 1.1;
  }
  .person-role {
    font-family: "Poppins", sans-serif;
    font-weight: 700;
    font-size: 12px;
    color: var(--green);
    letter-spacing: 1px;
  }
  .contacts {
    position: absolute;
    right: 30px; top: 112px;
    list-style: none;
    display: flex; flex-direction: column; gap: 12px;
  }
  .contact {
    display: flex; align-items: center; justify-content: flex-end; gap: 10px;
    font-size: 13px; color: var(--text-grey);
    text-align: right; line-height: 1.35;
    white-space: nowrap;
  }
  .contact-icon {
    width: 30px; height: 30px; border-radius: 50%;
    background: var(--ink);
    display: flex; align-items: center; justify-content: center;
    flex-shrink: 0;
  }
  .contact-icon svg { width: 16px; height: 16px; }
</style>
</head>
<body>

  <section class="card card-back" aria-label="Card back">
    <div class="back-pattern" role="img" aria-label="Repeating faint brand pattern on black"></div>
    <div class="back-brand">
      <span class="brand-square"></span>
      <span class="brand-name">DLQ MARROWFIELD</span>
    </div>
  </section>

  <section class="card card-front" aria-label="Card front">
    <svg class="front-shapes" viewBox="0 0 540 310" width="540" height="310" aria-hidden="true">
      <polygon points="60,20 120,20 110,36" fill="var(--card-black)"/>
      <polygon points="0,32 200,90 235,310 0,310" fill="var(--panel-dark)"/>
      <polygon points="70,42 200,90 258,125 240,310 200,310 225,150" fill="var(--green)"/>
      <polygon points="200,110 258,125 248,215" fill="var(--green-light)"/>
      <polygon points="268,255 305,310 278,310" fill="var(--green)"/>
    </svg>

    <div class="front-brand">
      <span class="brand-name">DLQ MARROWFIELD</span>
    </div>

    <div class="person">
      <p class="person-name">Henry Ashdown</p>
      <p class="person-role">DESIGNER</p>
    </div>

    <ul class="contacts">
      <li class="contact">
        <span>+000 123 456 789<br>+000 123 456 789</span>
        <span class="contact-icon">
          <svg viewBox="0 0 24 24"><path fill="var(--green)" d="M6.6 10.8a15 15 0 0 0 6.6 6.6l2.2-2.2c.3-.3.7-.4 1-.2 1.1.4 2.3.6 3.6.6.6 0 1 .4 1 1V20c0 .6-.4 1-1 1A17 17 0 0 1 3 4c0-.6.4-1 1-1h3.5c.6 0 1 .4 1 1 0 1.3.2 2.5.6 3.6.1.3 0 .7-.2 1z"/></svg>
        </span>
      </li>
      <li class="contact">
        <span>info@dlqmarrowfield.com.au</span>
        <span class="contact-icon">
          <svg viewBox="0 0 24 24" fill="none" stroke="var(--green)" stroke-width="2"><rect x="3" y="6" width="18" height="12"/><path d="M3 6l9 7 9-7"/></svg>
        </span>
      </li>
      <li class="contact">
        <span>Wrenmoor, Tasmania, Australia</span>
        <span class="contact-icon">
          <svg viewBox="0 0 24 24" fill="none" stroke="var(--green)" stroke-width="2"><path d="M3 11l9-7 9 7"/><path d="M6 10v10h12V10"/></svg>
        </span>
      </li>
    </ul>
  </section>

</body>
</html>
```